Quelto Marketing & Design needs a Wordpress website

We need a wordpress design for a new marketing and design company in Australia called 'Quelto Marketing & Design". The website needs to be responsive, modern, and attract new customers. It needs to be unique and different. We provide marketing and design solutions for small businesses from consulting, to flyer distribution to Facebook ads etc. We would like to see designs that use the Quelto logo colours. The final design should communicate professionalism, creativity & growth. It needs to stand out from the crowd.

Target Market(s)

Small Business who need a marketing freelancer to help them grow

Industry/Entity Type

Marketing

Number of Pages Required

3 page

Requirements
Must have
• Home page, services page & contact page

```html
<!DOCTYPE html>
<html lang="en">
<head>
<meta charset="utf-8">
<title>Quelto Marketing &amp; Design</title>
<link href="https://fonts.googleapis.com/css2?family=Roboto:wght@300;400;500;700;900&display=swap" rel="stylesheet">
<style>
:root{
  --purple:#3b2180;
  --purple-dark:#2a1862;
  --purple-deep:#1f1248;
  --pink:#e5177e;
  --ink:#2b2540;
  --text:#6b6878;
  --light:#f4f3f8;
  --white:#ffffff;
  --charcoal:#2b2832;
}
*{box-sizing:border-box;margin:0;padding:0}
html,body{width:1200px;height:3804px;overflow:hidden}
body{font-family:'Roboto',Arial,sans-serif;color:var(--text);background:var(--white);position:relative}
section,header,footer{position:relative;width:1200px;overflow:hidden}
.abs{position:absolute}
.btn-outline{display:inline-block;border:2px solid currentColor;padding:10px 20px;font-size:13px;font-weight:700;letter-spacing:1px}
.heading{font-size:32px;font-weight:900;color:var(--purple-dark);letter-spacing:.5px}
.heading-rule{width:70px;height:4px;background:var(--pink);margin-top:10px}

/* header / hero */
.hero{height:430px}
.hero-photo{position:absolute;inset:0;background:linear-gradient(120deg,#8a7aa8 0%,#c9b9cf 40%,#e8d6c8 70%,#b99ea9 100%)}
.brand{position:absolute;left:40px;top:18px;display:flex;align-items:center;gap:10px;color:var(--white)}
.brand-mark{width:34px;height:34px;border-radius:50%;background:var(--pink)}
.brand-name{font-size:30px;font-weight:700;line-height:1}
.brand-tag{font-size:10px;letter-spacing:1px;margin-top:3px}
.nav{position:absolute;right:40px;top:26px;display:flex;align-items:center;gap:4px}
.nav a{color:var(--white);font-size:12px;font-weight:700;padding:10px 18px;text-decoration:none;letter-spacing:.5px}
.nav a.active{background:var(--pink)}
.nav .phone{margin-left:12px;display:flex;align-items:center;gap:6px;color:var(--white);font-size:13px;font-weight:700}
.hero-title{position:absolute;right:40px;top:115px;text-align:right;color:var(--white)}
.hero-title h1{font-size:48px;font-weight:700}
.hero-title p{font-size:25px;margin-top:8px}
.hero-wave{position:absolute;left:0;bottom:0;width:1200px;height:260px}
.welcome{position:absolute;left:40px;top:245px;width:420px;color:var(--white)}
.welcome h2{font-size:38px;font-weight:900}
.welcome .rule{width:60px;height:4px;background:var(--pink);margin:8px 0 14px}
.welcome p{font-size:13px;line-height:1.6}
.welcome .btn-outline{margin-top:16px;padding:7px 14px;font-size:11px}

/* offer */
.offer{height:740px}
.offer-head{position:absolute;left:80px;top:40px}
.offer-aside{position:absolute;left:560px;top:54px;display:flex;align-items:center;gap:14px;font-size:13px;color:var(--text)}
.offer-aside span.line{width:50px;height:2px;background:var(--pink)}
.cards{position:absolute;left:80px;top:130px;display:flex;gap:46px}
.card{width:231px;height:570px;border-radius:116px;padding:22px;display:flex;flex-direction:column;align-items:center;text-align:center;color:var(--white)}
.card.purple{background:var(--purple)}
.card.pink{background:var(--pink)}
.card-icon{width:187px;height:187px;border-radius:50%;background:var(--white);display:flex;align-items:center;justify-content:center}
.card h3{font-size:17px;font-weight:900;margin-top:70px;letter-spacing:.5px}
.card p{font-size:13px;line-height:1.6;margin-top:14px;padding:0 14px}
.card .more{margin-top:auto;margin-bottom:58px;font-size:11px;font-weight:700;letter-spacing:1px}

/* who */
.who{height:232px}
.who-photo{position:absolute;inset:0;background:linear-gradient(90deg,var(--purple-dark) 0%,#5a3a9a 45%,#8f7bb5 75%,#b7a9c9 100%)}
.who-body{position:absolute;left:80px;top:36px;width:540px;color:var(--white)}
.who-body h2{font-size:30px;font-weight:900}
.who-body p{font-size:14px;line-height:1.6;margin-top:14px}
.who-body .btn-outline{margin-top:16px;padding:7px 14px;font-size:11px}

/* services */
.services{height:820px;background:var(--white)}
.services-head{position:absolute;left:80px;top:60px}
.services-intro{position:absolute;left:80px;top:140px;width:1040px;font-size:14px;line-height:1.6}
.service-cols{position:absolute;left:80px;top:230px;display:flex;gap:56px}
.service{width:310px}
.service-top{display:flex;gap:14px;align-items:flex-start}
.service-icon{flex:none;width:56px;height:56px;border-radius:50%;background:var(--pink);display:flex;align-items:center;justify-content:center}
.service h3{font-size:20px;font-weight:500;color:var(--pink);line-height:1.25;margin-top:4px}
.service h3.purple{color:var(--purple)}
.service p{font-size:13px;line-height:1.7;margin-top:20px}
.service .links{margin-top:22px;display:flex;gap:26px;font-size:11px;font-weight:700;color:var(--purple-dark);letter-spacing:.5px}
.services .btn-outline{position:absolute;left:80px;top:560px;color:var(--purple-dark);font-size:12px}

/* testimonials */
.testimonials{height:420px;background:var(--purple-dark)}
.testimonials .heading{color:var(--white)}
.testi-head{position:absolute;left:80px;top:40px}
.testi-arrows{position:absolute;right:80px;top:48px;display:flex;gap:22px}
.testi-intro{position:absolute;left:80px;top:120px;color:#d6cff0;font-size:14px}
.quotes{position:absolute;left:80px;top:170px;display:flex;gap:60px}
.quote{width:490px;color:#e3def4;font-size:13px;line-height:1.7}
.quote-by{display:flex;align-items:center;gap:16px;margin-top:26px}
.avatar{width:64px;height:64px;border-radius:50%;background:linear-gradient(135deg,#9c8fbf,#d6cbe2)}
.quote-by strong{display:block;color:var(--white);font-size:14px}
.quote-by span{font-size:12px;color:var(--pink)}

/* clients */
.clients{height:230px}
.client-row{position:absolute;left:80px;width:1040px;display:flex;justify-content:space-around;align-items:center}
.client{font-size:22px;font-weight:700;color:var(--purple-dark)}

/* contact info */
.contact-info{height:400px}
.map{position:absolute;inset:0;background:linear-gradient(135deg,#e5e5e8,#cfd0d4 55%,#e2e2e5)}
.info-box{position:absolute;left:410px;top:60px;width:380px;height:280px;background:var(--white);border:1px solid #ddd;padding:40px 40px;text-align:center}
.info-box h2{font-size:30px;font-weight:500;color:var(--ink)}
.info-box .heading-rule{margin:10px auto 26px}
.info-line{display:flex;align-items:center;justify-content:center;gap:10px;font-size:17px;color:var(--ink);margin-bottom:16px}
.info-line .hl{color:var(--pink)}

/* contact form */
.contact{height:480px;background:linear-gradient(180deg,#34303c,var(--charcoal))}
.contact h2{font-size:28px;font-weight:700;color:var(--white)}
.contact .heading-rule{margin:10px 0 18px}
.form-col{position:absolute;left:80px;top:50px;width:600px}
.form-col p{font-size:13px;color:#c3c0cb}
.fields{display:grid;grid-template-columns:1fr 1fr;gap:14px 22px;margin-top:20px}
.field{height:40px;border:1px solid #6a6672;padding:11px 14px;font-size:13px;color:#a8a4b0}
.field.wide{grid-column:1/3;height:90px}
.send{display:block;margin:22px 0 0 270px;width:240px;background:var(--pink);color:var(--white);text-align:center;padding:14px;font-size:14px;font-weight:700;letter-spacing:1px}
.address-col{position:absolute;left:720px;top:50px;width:400px;color:#c3c0cb;font-size:13px;line-height:1.8}
.address-col strong{color:var(--white);display:block;margin-bottom:4px}
.addr-line{display:flex;gap:10px;align-items:center;margin-top:10px}

/* footer */
.footer{height:64px;background:var(--white);border-top:1px solid #eee}
.footer .brand{top:14px;left:80px;color:var(--purple-dark)}
.footer .brand-name{font-size:24px}
.footer .brand-mark{width:28px;height:28px}
.copy{position:absolute;left:300px;top:24px;font-size:11px;color:var(--text)}
.socials{position:absolute;right:80px;top:22px;display:flex;gap:10px}
.socials span{width:20px;height:20px;border-radius:50%;background:var(--purple-dark)}
</style>
</head>
<body>

<header class="hero">
  <div class="hero-photo" role="img" aria-label="Photo of a designer's desk with laptop, notebooks and colour swatches"></div>
  <div class="brand">
    <div class="brand-mark"></div>
    <div><div class="brand-name">Quelto</div><div class="brand-tag">MARKETING &amp; DESIGN</div></div>
  </div>
  <nav class="nav">
    <a class="active">HOME</a><a>ABOUT</a><a>OUR SERVICES</a><a>WORK</a><a>CLIENTS</a><a>CONTACT US</a>
    <span class="phone">
      <svg width="14" height="14" viewBox="0 0 24 24"><path fill="#fff" d="M6.6 10.8a15 15 0 0 0 6.6 6.6l2.2-2.2a1 1 0 0 1 1-.3 11 11 0 0 0 3.6.6 1 1 0 0 1 1 1V20a1 1 0 0 1-1 1A17 17 0 0 1 3 4a1 1 0 0 1 1-1h3.5a1 1 0 0 1 1 1c0 1.3.2 2.5.6 3.6a1 1 0 0 1-.3 1z"/></svg>
      +1 800 555 0199
    </span>
  </nav>
  <div class="hero-title">
    <h1>Quelto Marketing &amp; Design</h1>
    <p>We are a marketing and design company in Australia</p>
  </div>
  <svg class="hero-wave" viewBox="0 0 1200 260" preserveAspectRatio="none">
    <path d="M0 0 L520 0 C620 40 680 120 760 170 C880 240 1040 220 1200 150 L1200 260 L0 260Z" fill="#3b2180" opacity=".92"/>
    <path d="M0 150 C300 250 700 260 1200 190 L1200 260 L0 260Z" fill="#e5177e" opacity=".9"/>
    <path d="M0 200 C320 270 760 270 1200 215 L1200 260 L0 260Z" fill="#ffffff"/>
  </svg>
  <div class="welcome">
    <h2>WELCOME !</h2>
    <div class="rule"></div>
    <p>We help small businesses grow with clear strategy, bold design and marketing that works. From your first logo to your next big campaign, we are right beside you.</p>
    <span class="btn-outline">LEARN MORE &gt;</span>
  </div>
</header>

<section class="offer">
  <div class="offer-head"><h2 class="heading">WHAT WE OFFER</h2><div class="heading-rule"></div></div>
  <div class="offer-aside"><span class="line"></span>Find out more about what services and packages we offer</div>
  <div class="cards">
    <article class="card purple">
      <div class="card-icon"><svg width="70" height="70" viewBox="0 0 24 24"><path fill="#3b2180" d="M12 2l6 8-6 12-6-12z"/><circle cx="12" cy="10" r="1.8" fill="#fff"/></svg></div>
      <h3>LOGO DESIGN</h3>
      <p>A memorable mark built around your story, ready for print, web and signage.</p>
      <span class="more">LEARN MORE &gt;</span>
    </article>
    <article class="card pink">
      <div class="card-icon"><svg width="76" height="76" viewBox="0 0 24 24"><rect x="2" y="5" width="20" height="14" rx="2" fill="#e5177e"/><rect x="4.5" y="8" width="6" height="7" fill="#fff"/><rect x="12.5" y="9" width="7" height="1.6" fill="#fff"/><rect x="12.5" y="12.5" width="5" height="1.6" fill="#fff"/></svg></div>
      <h3>CORPORATE IDENTITY</h3>
      <p>Business cards, letterheads and brand guides that keep you consistent.</p>
      <span class="more">LEARN MORE &gt;</span>
    </article>
    <article class="card purple">
      <div class="card-icon"><svg width="72" height="72" viewBox="0 0 24 24"><rect x="3" y="6" width="12" height="15" fill="#3b2180"/><rect x="8" y="3" width="12" height="15" fill="#5a3ea6"/><rect x="10" y="6" width="8" height="1.5" fill="#fff"/><rect x="10" y="9" width="8" height="1.5" fill="#fff"/><rect x="10" y="12" width="5" height="1.5" fill="#fff"/></svg></div>
      <h3>FLYERS</h3>
      <p>Eye-catching flyers designed, printed and distributed to your local area.</p>
      <span class="more">LEARN MORE &gt;</span>
    </article>
    <article class="card pink">
      <div class="card-icon"><svg width="76" height="76" viewBox="0 0 24 24"><path fill="#e5177e" d="M3 4h12v8H8l-3 3v-3H3z"/><path fill="#3b2180" d="M10 13h5v-3h6v8h-2v3l-3-3h-6z"/></svg></div>
      <h3>CONSULTING</h3>
      <p>Honest advice and a practical plan to reach the customers you want.</p>
      <span class="more">LEARN MORE &gt;</span>
    </article>
  </div>
</section>

<section class="who">
  <div class="who-photo" role="img" aria-label="Photo of a team working together around a laptop, under a purple tint"></div>
  <div class="who-body">
    <h2>WHO IS QUELTO MARKETING &amp; DESIGN?</h2>
    <p>Quelto Marketing and Design is a boutique marketing and design venture in Perth, WA. We're here for you, that's why we get results for our clients.</p>
    <span class="btn-outline">LEARN MORE &gt;</span>
  </div>
</section>

<section class="services">
  <div class="services-head"><h2 class="heading">OUR SERVICES</h2><div class="heading-rule"></div></div>
  <p class="services-intro">Quelto Marketing and Design offers a wide range of services for your individual business needs. Whether you are just starting up or have been in the market for years we can offer a tailored service just for you.</p>
  <div class="service-cols">
    <div class="service">
      <div class="service-top">
        <div class="service-icon"><svg width="26" height="26" viewBox="0 0 24 24"><path fill="#fff" d="M9 16.2 4.8 12l-1.4 1.4L9 19 21 7l-1.4-1.4z"/></svg></div>
        <h3>Just starting up?</h3>
      </div>
      <p>Congratulations, you have taken the first step to success; now you just need to look the part. There is only a logo and stationery package away from you.</p>
      <div class="links"><span>VIEW PACKAGE &gt;</span><span>CONTACT &gt;</span></div>
    </div>
    <div class="service">
      <div class="service-top">
        <div class="service-icon"><svg width="26" height="26" viewBox="0 0 24 24"><path fill="#fff" d="M3 17l6-6 4 4 8-8v4h2V3h-8v2h4l-6 6-4-4-8 8z"/></svg></div>
        <h3 class="purple">Need a marketing boost or revamp?</h3>
      </div>
      <p>If your business has been running for a while and you are ready to boost your sales then you might want to look at flyers or direct marketing.</p>
      <div class="links"><span>VIEW PACKAGE &gt;</span><span>CONTACT &gt;</span></div>
    </div>
    <div class="service">
      <div class="service-top">
        <div class="service-icon"><svg width="26" height="26" viewBox="0 0 24 24"><path fill="#fff" d="M4 4h16v11H8l-4 4z"/></svg></div>
        <h3>Marketing Consulting or Advise</h3>
      </div>
      <p>If you just need some solid advice on marketing tips or what you can do as a business then consulting is for you. Let us guide your next move.</p>
      <div class="links"><span>VIEW PACKAGE &gt;</span><span>CONTACT &gt;</span></div>
    </div>
  </div>
  <span class="btn-outline">VIEW OUR FULL RANGE OF SERVICES &gt;</span>
</section>

<section class="testimonials">
  <div class="testi-head"><h2 class="heading">CLIENT TESTIMONIALS</h2><div class="heading-rule"></div></div>
  <div class="testi-arrows">
    <svg width="14" height="22" viewBox="0 0 14 22"><path d="M12 2 3 11l9 9" stroke="#fff" stroke-width="3" fill="none"/></svg>
    <svg width="14" height="22" viewBox="0 0 14 22"><path d="m2 2 9 9-9 9" stroke="#fff" stroke-width="3" fill="none"/></svg>
  </div>
  <p class="testi-intro">Thanks to our clients, without you we wouldn't be where we are today.</p>
  <div class="quotes">
    <div class="quote">
      <p>"Working with the team was easy from day one. They listened, asked the right questions and delivered a brand we are proud of. Our new flyers brought in more enquiries in a month than we had all year. Friendly, fast and always on time. Highly recommended."</p>
      <div class="quote-by"><div class="avatar" role="img" aria-label="Client portrait"></div><div><strong>Dana Irwin</strong><span>Business Owner</span></div></div>
    </div>
    <div class="quote">
      <p>"We needed a fresh look and a clear plan for growth. The consulting sessions gave us real direction and the new website looks fantastic. Our customers notice the difference and so do we. Great people to work with on any project, big or small."</p>
      <div class="quote-by"><div class="avatar" role="img" aria-label="Client portrait"></div><div><strong>Dana Irwin</strong><span>Business Owner</span></div></div>
    </div>
  </div>
</section>

<section class="clients">
  <div class="client-row" style="top:40px">
    <span class="client">Ardmore</span><span class="client">Velco</span><span class="client">Brellow</span><span class="client">Pinlo</span><span class="client">Sportiq</span><span class="client">Fizzmont</span><span class="client">Brightwell</span><span class="client">Karuvo</span>
  </div>
  <div class="client-row" style="top:130px;left:300px;width:600px">
    <span class="client">Tenvix</span><span class="client">Kastro</span><span class="client">Rivo</span><span class="client">Halden</span>
  </div>
</section>

<section class="contact-info">
  <div class="map" role="img" aria-label="Street map showing the office location"></div>
  <div class="info-box">
    <h2>CONTACT Info</h2>
    <div class="heading-rule"></div>
    <div class="info-line">
      <svg width="18" height="18" viewBox="0 0 24 24"><path fill="#2b2540" d="M6.6 10.8a15 15 0 0 0 6.6 6.6l2.2-2.2a1 1 0 0 1 1-.3 11 11 0 0 0 3.6.6 1 1 0 0 1 1 1V20a1 1 0 0 1-1 1A17 17 0 0 1 3 4a1 1 0 0 1 1-1h3.5a1 1 0 0 1 1 1c0 1.3.2 2.5.6 3.6a1 1 0 0 1-.3 1z"/></svg>
      <span>Telephone: +1 800 555 0199</span>
    </div>
    <div class="info-line">
      <svg width="18" height="18" viewBox="0 0 24 24"><path fill="#2b2540" d="M2 5h20v14H2zm2 2v.5l8 5 8-5V7z"/></svg>
      <span>E-mail: <span class="hl">hello@quelto.example</span></span>
    </div>
  </div>
</section>

<section class="contact">
  <div class="form-col">
    <h2>CONTACT FORM</h2>
    <div class="heading-rule"></div>
    <p>We'd love to hear from you so why don't you get in touch?</p>
    <div class="fields">
      <div class="field">Enter Name</div>
      <div class="field">Enter Email Address</div>
      <div class="field">Subject</div>
      <div class="field">Contact No</div>
      <div class="field wide">Type Message Here</div>
    </div>
    <span class="send">SEND US MESSAGE</span>
  </div>
  <div class="address-col">
    <h2>CONTACT ADDRESS</h2>
    <div class="heading-rule"></div>
    <strong>QUELTO MARKETING &amp; DESIGN</strong>
    <div>14 Harbour Lane, Suite 2<br>Perth WA 6000</div>
    <div class="addr-line">
      <svg width="14" height="14" viewBox="0 0 24 24"><path fill="#e5177e" d="M6.6 10.8a15 15 0 0 0 6.6 6.6l2.2-2.2a1 1 0 0 1 1-.3 11 11 0 0 0 3.6.6 1 1 0 0 1 1 1V20a1 1 0 0 1-1 1A17 17 0 0 1 3 4a1 1 0 0 1 1-1h3.5a1 1 0 0 1 1 1c0 1.3.2 2.5.6 3.6a1 1 0 0 1-.3 1z"/></svg>
      <span>Tel: +1 800 555 0199</span>
    </div>
    <div class="addr-line">
      <svg width="14" height="14" viewBox="0 0 24 24"><path fill="#e5177e" d="M2 5h20v14H2zm2 2v.5l8 5 8-5V7z"/></svg>
      <span>E-mail: hello@quelto.example</span>
    </div>
  </div>
</section>

<footer class="footer">
  <div class="brand">
    <div class="brand-mark"></div>
    <div class="brand-name">Quelto</div>
  </div>
  <span class="copy">© 2024 Quelto. All Rights Reserved.</span>
  <div class="socials"><span></span><span></span><span></span><span></span></div>
</footer>

</body>
</html>
```